Presentation card Venture KELO - Tech Incubator from Perú

We need a Design to promote the incubator of technology Startups.
We are in Perú, we work with a string tech filter and develop enterprenurship competencies in the Startup team.
The card is to facilitators and staff memebers of VentureKELO.
We want a clear, modern, tech and agile Design.

We work to help New enterprises of technology here in Perú, we expect the candidates have a big competencies to Research and develop technological products.

We work using methodologies from QRB, Folmestry, Brakewell and Harrowgate univeesities. Our book base is the disciplina of enterpreneur.

We work events all year using diferent formats: Brightforge, Vorne price, OPRA Model Competition you can use these logros in your Design.

Set the name, role, email, cell phone number, address.

Example:
// Contact info section
Tobías Quiroveda
Swift Modeling Hub Manager
tobias.quiroveda@kelo-example.pe
(511) 999 000 417

// Address info section
VentureKELO
Technology-based business incubator
Av. Los Cedrales 884, Valdora
Lima - Perú
web: venture-kelo-example.org.pe
email: venture@kelo-example.pe
phone number: (511) 3926508 ext. 4418

// (optional)Lema section
Making happy using technology

// Social network section
facebook: venturekelooficial

Target Market(s)

Enterprenurship, CTO, Investors, Companies interested on open innovation services

Industry/Entity Type

Information Technology

Contact Information for Business Card

Name, Role, Email, Cell phone number

Colors

Designer to choose colors to be used in the design.

Requirements
Must have
• Logo forms and colors
Nice to have
• I add pictures of the leaders of incubator
Should not have
• No vertical designs

```html
<!DOCTYPE html>
<html lang="en">
<head>
<meta charset="utf-8">
<title>VentureKELO – Business Card</title>
<link rel="stylesheet" href="https://fonts.googleapis.com/css2?family=Quicksand:wght@400;500;700&display=swap">
<style>
  :root {
    --crimson: #9e2747;
    --crimson-light: #b8445f;
    --paper: #f7f7f8;
    --ink: #2a2a2e;
    --muted: #7a7a80;
    --stage: #dfe3e8;
  }
  * { box-sizing: border-box; margin: 0; padding: 0; }
  html, body { width: 1200px; height: 675px; overflow: hidden; }
  body {
    background: var(--stage);
    font-family: "Quicksand", sans-serif;
    display: flex; align-items: center; justify-content: center; gap: 40px;
  }
  .card {
    position: relative; width: 540px; height: 309px; overflow: hidden;
    background: var(--paper);
    box-shadow: 0 10px 28px rgba(40, 50, 70, .18);
  }

  /* Back side */
  .back-wedge { position: absolute; inset: 0; }
  .back-info { position: absolute; left: 190px; right: 24px; top: 54px; }
  .back-name {
    font-weight: 700; font-size: 24px; color: var(--ink);
    text-align: center; letter-spacing: .5px;
  }
  .back-tagline {
    margin-top: 6px; font-size: 20px; color: var(--crimson);
    text-align: center; padding-bottom: 8px;
    border-bottom: 1px solid rgba(0,0,0,.12);
  }
  .contact-list { list-style: none; margin: 20px 0 0 62px; }
  .contact-list li {
    display: flex; align-items: center; gap: 10px;
    font-size: 10.5px; color: var(--muted); line-height: 19px;
  }
  .contact-list svg { width: 11px; height: 11px; flex: none; fill: var(--crimson); }

  /* Front side */
  .front-brand {
    position: absolute; left: 0; top: 0; bottom: 0; width: 215px;
    display: flex; align-items: center; justify-content: center; gap: 10px;
  }
  .brand-square { width: 16px; height: 16px; background: var(--crimson); }
  .brand-name { font-weight: 700; font-size: 26px; color: var(--ink); line-height: 1.05; }
  .front-panel {
    position: absolute; left: 215px; right: 0; top: 0; bottom: 0;
    background: linear-gradient(135deg, var(--crimson-light), var(--crimson));
    box-shadow: -6px 0 12px rgba(0,0,0,.18);
    color: #fff; padding: 78px 30px 0 58px;
  }
  .person-name { font-weight: 500; font-size: 19px; letter-spacing: .3px; }
  .person-role {
    font-size: 11px; opacity: .85; margin-top: 10px; padding-top: 10px;
    border-top: 1px solid rgba(255,255,255,.35);
  }
  .front-contacts { list-style: none; margin-top: 30px; }
  .front-contacts li {
    display: flex; align-items: center; gap: 18px;
    font-size: 11px; line-height: 28px; opacity: .92;
  }
  .front-contacts svg { width: 13px; height: 13px; fill: #fff; flex: none; }
</style>
</head>
<body>

<section class="card card-back">
  <svg class="back-wedge" viewBox="0 0 540 309" preserveAspectRatio="none" aria-hidden="true">
    <polygon points="0,0 78,0 238,309 0,309" fill="var(--crimson)"/>
  </svg>
  <div class="back-info">
    <h1 class="back-name">VentureKELO</h1>
    <p class="back-tagline">Technology-based business incubator</p>
    <ul class="contact-list">
      <li><svg viewBox="0 0 12 12"><path d="M3 1l2 2.5-1.2 1.3a7 7 0 0 0 3.4 3.4L8.5 7 11 9l-1.5 2C5 11 1 7 1 2.5z"/></svg>(511) 3926508 ext. 4418</li>
      <li><svg viewBox="0 0 12 12"><path d="M1 3h10v6H1zM1 3l5 3.5L11 3"/></svg>venture@kelo-example.pe</li>
      <li><svg viewBox="0 0 12 12"><circle cx="6" cy="6" r="5"/></svg>venture-kelo-example.org.pe</li>
      <li><svg viewBox="0 0 12 12"><rect x="1.5" y="1.5" width="9" height="9"/></svg>venturekelooficial</li>
      <li><svg viewBox="0 0 12 12"><path d="M6 1a3.5 3.5 0 0 1 3.5 3.5C9.5 7 6 11 6 11S2.5 7 2.5 4.5A3.5 3.5 0 0 1 6 1z"/></svg>Av. Los Cedrales 884, Valdora<br>Lima - Perú</li>
    </ul>
  </div>
</section>

<section class="card card-front">
  <div class="front-brand">
    <span class="brand-square" aria-hidden="true"></span>
    <span class="brand-name">Venture<br>KELO</span>
  </div>
  <div class="front-panel">
    <h2 class="person-name">Tobías Quiroveda</h2>
    <p class="person-role">Swift Modeling Hub Manager</p>
    <ul class="front-contacts">
      <li><svg viewBox="0 0 12 12"><path d="M3 1l2 2.5-1.2 1.3a7 7 0 0 0 3.4 3.4L8.5 7 11 9l-1.5 2C5 11 1 7 1 2.5z"/></svg>(511) 999 000 417</li>
      <li><svg viewBox="0 0 12 12"><path d="M1 2.5h10v7H1zm0 0l5 4 5-4" stroke="var(--crimson)" stroke-width=".8"/></svg>tobias.quiroveda@kelo-example.pe</li>
    </ul>
  </div>
</section>

</body>
</html>
```